Flyer-Design für Zauber-Projekt
Sehr netter und kreativer Kontakt, alle Änderungswünsche wurden kurzfristig umgesetzt, vielen Dank! Meine Flyer gefallen mir super gut! :-)
Zielgruppe
Ich bin Zauberkünstlerin und auf der Suche nach Flyern für ein spezielles Projekt. Dabei handelt es sich um das vermutlich kleinste Zaubertheater der Welt- eine Art Box, die sehr vintage aussieht (wie ein Relikt aus dem 19. Jahrhundert). Wirft man Geld in den Münzschlitz, öffnen sich die Türen des 'Pling-E-Tor' und ich unterhalte das Publikum mit erstaunlichen Zaubereien :-) Zielgruppe sind Firmen, die eine Kunden- und Gäste-Unterhaltung für ihre Messe- oder andere Kundenveranstaltungen (z.B. Tag der offenen Türe, Jubiläen, ...) suchen, oder Kulturschaffende wie Varietès, Theater, Museen etc, in denen der Pling-E-Tor im Wartebereich stehen könnte.
Aufgabenstellung
Der Flyer sollte gerne im 'Vintage-Style' sein, um die 'Magie' des Pling-e-Tor zu transportieren und dennoch ansprechend auf Firmen wirken, d.h. eine Mischung aus Vintage und 'Modern-Professionell' wäre ideal. Weiteres Bildmaterial stelle ich gerne zur Verfügung. Als Schriftart finde ich 'Chopin' oder 'Rochester' sehr schön, vielleicht für die Überschriften?

```html
<!DOCTYPE html>
<html lang="de">
<head>
<meta charset="utf-8">
<title>Pling-E-Tor Flyer</title>
<link rel="stylesheet" href="https://fonts.googleapis.com/css2?family=Fondamento&family=EB+Garamond:wght@400;700&display=swap">
<style>
  :root {
    --bg: #e6e2e0;
    --wood-dark: #3e3128;
    --wood-mid: #6b5a4b;
    --wood-light: #8a7764;
    --parchment-light: #f4dca6;
    --parchment-mid: #e9b969;
    --parchment-dark: #c98a3c;
    --red: #b5202a;
    --red-dark: #8c1a20;
    --ink: #1b1410;
    --white: #ffffff;
    --photo-tone-a: #8f8a86;
    --photo-tone-b: #2c2226;
  }
  * { box-sizing: border-box; margin: 0; padding: 0; }
  html, body { width: 1200px; height: 800px; overflow: hidden; }
  body {
    background: var(--bg);
    font-family: "EB Garamond", Georgia, serif;
    color: var(--ink);
    position: relative;
  }
  .flyer {
    position: absolute;
    top: 117px;
    width: 400px;
    height: 566px;
    background:
      repeating-linear-gradient(90deg, var(--wood-mid) 0 38px, var(--wood-dark) 38px 40px, var(--wood-light) 40px 78px, var(--wood-dark) 78px 80px);
    box-shadow: 0 10px 30px rgba(0,0,0,.25);
    overflow: hidden;
  }
  .flyer--back { left: 170px; }
  .flyer--front { left: 630px; }
  .parchment {
    position: absolute;
    inset: 18px;
    background: radial-gradient(ellipse at 50% 40%, var(--parchment-light), var(--parchment-mid) 65%, var(--parchment-dark));
  }

  /* Back side */
  .back-title {
    font-family: "Fondamento", serif;
    font-size: 22px;
    line-height: 1.15;
    text-align: center;
    margin: 18px 10px 10px;
  }
  .back-copy {
    font-size: 9.6px;
    line-height: 1.38;
    text-align: center;
    padding: 0 18px;
  }
  .back-copy p { margin-bottom: 8px; }
  .back-copy h3 { font-size: 10px; font-weight: 700; margin-bottom: 1px; }
  .contact-band {
    position: absolute;
    left: 0; right: 0; bottom: 0;
    height: 104px;
  }
  .contact-band svg { position: absolute; inset: 0; }
  .contact-name {
    position: absolute;
    left: 24px; bottom: 20px;
    font-family: "Fondamento", serif;
    font-size: 20px;
    line-height: 1.1;
    color: var(--white);
  }
  .contact-lines {
    position: absolute;
    left: 120px; bottom: 22px;
    font-size: 9.5px;
    line-height: 1.55;
    font-weight: 700;
    color: var(--white);
  }
  .portrait {
    position: absolute;
    right: 6px; bottom: 8px;
    width: 100px; height: 150px;
    background: linear-gradient(180deg, #5a3a2c, var(--photo-tone-b));
    border-radius: 4px 4px 0 0;
  }

  /* Front side */
  .logo-band {
    position: absolute;
    left: 0; right: 0; top: 8px;
    height: 64px;
    background: var(--white);
    display: flex; align-items: center; justify-content: center;
  }
  .logo-name {
    font-family: "Fondamento", serif;
    font-size: 30px;
    color: var(--ink);
  }
  .hero {
    position: absolute;
    left: 28px; top: 98px;
    width: 308px; height: 208px;
  }
  .hero-layer {
    position: absolute;
    background: var(--red);
  }
  .hero-layer--1 { inset: -10px 8px 14px -6px; transform: rotate(-3deg); }
  .hero-layer--2 { inset: 12px -10px -8px 14px; background: var(--parchment-dark); transform: rotate(2deg); }
  .hero-photo {
    position: absolute; inset: 0;
    background: linear-gradient(135deg, #e6e2d8, var(--photo-tone-a) 55%, var(--photo-tone-b));
    border: 3px solid var(--white);
  }
  .headline {
    position: absolute;
    left: 0; right: 0; top: 318px;
    text-align: center;
    font-family: "Fondamento", serif;
    font-size: 28px;
  }
  .ribbon {
    position: absolute;
    left: -4px; top: 360px;
    width: 372px; height: 58px;
  }
  .ribbon-text {
    position: absolute;
    left: 0; right: 0; top: 370px;
    text-align: center;
    font-family: "Fondamento", serif;
    font-size: 27px;
    color: var(--white);
  }
  .snapshot {
    position: absolute;
    width: 100px; height: 74px;
    border: 4px solid var(--white);
    box-shadow: 0 2px 5px rgba(0,0,0,.3);
  }
  .snapshot--1 { left: 18px; top: 440px; transform: rotate(-4deg); background: linear-gradient(135deg, #d9d2c4, #8e6a4a); }
  .snapshot--2 { left: 126px; top: 446px; transform: rotate(5deg); background: linear-gradient(135deg, #f1eee6, #b8994a); }
  .snapshot--3 { left: 232px; top: 440px; transform: rotate(-2deg); background: linear-gradient(135deg, #b9b4ae, #6d2028); }
</style>
</head>
<body>

<section class="flyer flyer--back">
  <div class="parchment">
    <h2 class="back-title">Was ist denn bitte ein …<br>Pling-E-Tor?</h2>
    <div class="back-copy">
      <p>Der Pling-E-Tor ist das wahrscheinlich kleinste Zaubertheater der Welt, in dem Lady Rosalind ihr Publikum in die faszinierende Welt der Magie entführt. Verblüffende Tricks direkt vor den Augen und sogar in den Händen der Zuschauer – ein ganz besonderes Erlebnis, das lange in Erinnerung bleibt!</p>
      <h3>Der Pling-E-Tor auf Ihrem Event.</h3>
      <p>Mieten Sie den Pling-E-Tor für Ihre Messe- oder andere Kundenveranstaltungen, den Tag der offenen Tür oder für die Unterhaltung Ihrer Gäste bei großen Hochzeiten, Jubiläen und anderen Feierlichkeiten. Oder für den Wartebereich von Theatern, Museen, Varietés oder anderen Veranstaltungsorten. Der Pling-E-Tor begeistert überall dort, wo Kunden und Gäste mit Ihrer Firma Aufmerksamkeit erregen wollen oder Sie ein besonderes Erlebnis bieten möchten.</p>
      <p>Mit viel kreativem Herzblut in Eigenregie gestaltet, ist er ein optischer Blickfang jede Veranstaltung. Die geheimnisvolle Box verbindet Publikum mit charmant-humorvoller Zauberei an ihren Sinnen und macht den Pling-E-Tor zu einem faszinierenden Gesamtkunstwerk.</p>
      <h3>Werbung, die Ihre Kunden verzaubert.</h3>
      <p>Buchen Sie den Pling-E-Tor für Ihre Messe oder Veranstaltung und stellen Sie eine „magische“ Verbindung zu Ihrer Firma her. Kombinieren Sie den Pling-E-Tor mit Ihren Aufstellern, Beachflags oder Bannern – eine zauberhafte Verknüpfung zwischen Ihrer Firma und dem Kunden-Publikum ist garantiert! Gerne beraten wir Sie über geeignetes Werbematerial.</p>
    </div>
    <div class="contact-band">
      <svg viewBox="0 0 364 104" preserveAspectRatio="none" aria-hidden="true">
        <path d="M0 34 L70 30 L150 24 L240 18 L364 12 L364 104 L0 104 Z" fill="var(--red)"/>
        <path d="M0 92 L364 86 L364 92 L0 98 Z" fill="var(--white)" opacity=".85"/>
      </svg>
      <div class="portrait" role="img" aria-label="Foto der Zauberkünstlerin im schwarzen Kleid mit Kerze"></div>
      <div class="contact-name">Petra<br>Kux</div>
      <div class="contact-lines">
        Telefon : 0171/2 34 56 78<br>
        Email : petra@zauberwerkstatt.in<br>
        Web : www.pling-e-tor.de
      </div>
    </div>
  </div>
</section>

<section class="flyer flyer--front">
  <div class="parchment">
    <div class="logo-band"><span class="logo-name">Pling-E-Tor</span></div>
    <div class="hero">
      <div class="hero-layer hero-layer--2"></div>
      <div class="hero-layer hero-layer--1"></div>
      <div class="hero-photo" role="img" aria-label="Foto: Zauberkünstlerin im geöffneten, verzierten Miniaturtheater mit roter Samtbrüstung"></div>
    </div>
    <h1 class="headline">Türen auf- lassen</h1>
    <svg class="ribbon" viewBox="0 0 372 58" aria-hidden="true">
      <path d="M0 8 L372 4 L360 30 L372 54 L0 58 L12 32 Z" fill="var(--red)"/>
    </svg>
    <div class="ribbon-text">Sie sich verzaubern!</div>
    <div class="snapshot snapshot--1" role="img" aria-label="Foto: Schriftzug auf dem Theaterkasten"></div>
    <div class="snapshot snapshot--2" role="img" aria-label="Foto: Hand wirft Münze in den Schlitz"></div>
    <div class="snapshot snapshot--3" role="img" aria-label="Foto: Zauberkünstlerin zeigt Gästen einen Trick"></div>
  </div>
</section>

</body>
</html>
```